Ceiling fan flyer design

We are after a double sided flyer design offering ceiling fan installations

Target Market(s)

Home owners

Requirements
Must have
• content listed

```html
<!DOCTYPE html>
<html lang="en">
<head>
<meta charset="utf-8">
<title>Ceiling Fan Flyer – Front and Back</title>
<link rel="stylesheet" href="https://fonts.googleapis.com/css2?family=Titan+One&family=Anton&family=Oswald:wght@500;600;700&family=Open+Sans:ital,wght@0,400;0,600;0,700;1,400;1,600;1,700&family=Rubik:wght@500;700&display=swap">
<style>
  :root {
    --maroon: #741d1e;
    --maroon-dark: #5e1415;
    --cream: #fffbe6;
    --cream-edge: #f5ecc2;
    --heading-cream: #fff6cf;
    --yellow: #fff200;
    --hot-top: #fff45a;
    --hot-bottom: #f08a1c;
    --green: #13683a;
    --green-title: #0e5a2c;
    --orange: #e8731c;
    --text: #4a4a4a;
    --white: #ffffff;
    --backdrop: #e9e9e9;
  }
  * { box-sizing: border-box; margin: 0; padding: 0; }
  html, body { width: 1200px; height: 1000px; overflow: hidden; }
  body { background: var(--backdrop); font-family: "Open Sans", Arial, sans-serif; position: relative; }

  .flyer {
    position: absolute; top: 120px; width: 536px; height: 760px;
    background: var(--cream);
    box-shadow: 0 6px 18px rgba(0,0,0,.28);
    overflow: hidden;
  }
  .flyer--front { left: 52px; }
  .flyer--back { left: 613px; }

  .flyer__header {
    position: absolute; left: 0; top: 0; width: 100%; height: 142px;
    background: var(--maroon);
  }
  .headline {
    position: absolute; left: 48px; top: 14px;
    font-family: "Titan One", "Arial Black", sans-serif; font-style: italic;
    color: var(--heading-cream); line-height: 1;
    text-shadow: 0 2px 3px rgba(0,0,0,.35);
  }
  .headline__top { font-size: 64px; letter-spacing: -1px; white-space: nowrap; }
  .headline__hot {
    background: linear-gradient(var(--hot-top) 30%, var(--hot-bottom) 95%);
    -webkit-background-clip: text; background-clip: text; color: transparent;
    text-shadow: none;
  }
  .headline__bottom { font-size: 47px; margin-top: -2px; letter-spacing: -0.5px; }

  .flyer__body {
    position: absolute; left: 0; top: 142px; width: 100%; height: 516px;
    background: radial-gradient(ellipse at 50% 50%, var(--cream) 60%, var(--cream-edge) 100%);
  }

  .flyer__footer {
    position: absolute; left: 0; bottom: 0; width: 100%; height: 102px;
    background: var(--maroon);
  }
  .brand {
    position: absolute; left: 26px; top: 0; width: 96px; height: 102px;
    background: var(--white);
    display: flex; flex-direction: column; align-items: center; justify-content: center; gap: 6px;
  }
  .brand__mark { width: 18px; height: 18px; background: var(--maroon); }
  .brand__name {
    font-family: "Rubik", Arial, sans-serif; font-weight: 700; font-size: 15px;
    color: var(--maroon); text-align: center; line-height: 1.1;
  }
  .contact { position: absolute; left: 140px; top: 22px; }
  .contact__phone {
    font-family: "Rubik", Arial, sans-serif; font-weight: 700; font-size: 40px;
    color: var(--yellow); line-height: 1; letter-spacing: -0.5px;
  }
  .contact__web { color: var(--white); font-size: 14px; margin-top: 5px; letter-spacing: .3px; }
  .footer-divider { position: absolute; left: 408px; top: 26px; width: 1px; height: 52px; background: var(--white); }
  .payments { position: absolute; left: 420px; top: 30px; display: flex; gap: 4px; }
  .payments span { width: 31px; height: 22px; border-radius: 2px; border: 1px solid var(--white); }
  .payments .pay-a { background: #c9462a; }
  .payments .pay-b { background: #f2f2f2; }
  .payments .pay-c { background: #5b8fc7; }
  .licence { position: absolute; left: 421px; top: 64px; color: var(--white); font-size: 12.5px; }

  /* Front */
  .fan-photo {
    position: absolute; left: 40px; top: 0; width: 456px; height: 180px;
    background: radial-gradient(ellipse at 50% 55%, #e7e1cf 0%, #d6cfb8 35%, rgba(255,251,230,0) 70%);
  }
  .offer {
    position: absolute; left: 28px; top: 193px; width: 478px; height: 198px;
    background: var(--green); border: 2px dashed #d9c64a;
  }
  .offer__dollar {
    position: absolute; left: 12px; top: 54px;
    font-family: "Anton", sans-serif; font-size: 44px; color: var(--yellow); line-height: 1;
  }
  .offer__save {
    position: absolute; left: 54px; top: 4px;
    font-family: "Anton", sans-serif; font-size: 60px; color: var(--white); line-height: 1; letter-spacing: -1px;
  }
  .offer__amount {
    position: absolute; left: 40px; top: 50px;
    font-family: "Anton", sans-serif; font-size: 142px; color: var(--yellow); line-height: 1; letter-spacing: -6px;
  }
  .offer__off {
    position: absolute; left: 219px; top: 128px; transform-origin: left top; transform: rotate(-90deg);
    font-family: "Anton", sans-serif; font-size: 54px; color: var(--white); line-height: 1;
  }
  .offer__divider { position: absolute; left: 276px; top: 22px; width: 1px; height: 152px; background: var(--white); }
  .offer__deal {
    position: absolute; left: 286px; top: 10px; width: 180px; text-align: center;
    font-family: "Oswald", sans-serif; font-weight: 600; color: var(--white); font-size: 31px; line-height: 1.06;
  }
  .offer__deal sup { font-size: 16px; vertical-align: 12px; }
  .offer__terms {
    position: absolute; left: 282px; top: 126px; width: 190px; text-align: center;
    color: var(--white); font-size: 11.5px; line-height: 1.35;
  }
  .offer__terms strong { font-weight: 700; }
  .pitch { position: absolute; left: 30px; top: 403px; width: 476px; text-align: center; }
  .pitch__title { font-weight: 700; font-size: 22px; color: var(--maroon); }
  .pitch__text { font-size: 17.5px; color: var(--text); line-height: 1.4; margin-top: 2px; }

  /* Back */
  .promises { position: absolute; left: 46px; top: 30px; }
  .promises__title { font-weight: 700; font-size: 21px; color: var(--green-title); line-height: 1.1; }
  .promises__list { list-style: none; font-size: 14.8px; color: var(--text); line-height: 22px; margin-top: 2px; }
  .promises__list li { position: relative; padding-left: 10px; }
  .promises__list li::before {
    content: ""; position: absolute; left: 0; top: 9px; width: 5px; height: 5px; border-radius: 50%; background: var(--orange);
  }
  .promises__list .indent { padding-left: 10px; }
  .promises__list strong { color: var(--maroon); }
  .rule { position: absolute; left: 46px; top: 274px; width: 364px; border-top: 1px dotted #c8c0a0; }
  .reviews { position: absolute; left: 46px; top: 302px; width: 470px; }
  .review { margin-bottom: 22px; }
  .review__quote { font-style: italic; font-size: 17.5px; color: var(--text); line-height: 1.35; }
  .review__name { font-style: italic; font-weight: 700; font-size: 17px; color: var(--maroon); line-height: 1.4; }
  .review__place { font-style: italic; font-weight: 700; font-size: 17px; color: var(--orange); line-height: 1.4; }
</style>
</head>
<body>

<section class="flyer flyer--front">
  <header class="flyer__header">
    <h1 class="headline">
      <div class="headline__top"><span class="headline__hot">Hot</span> Sweaty</div>
      <div class="headline__bottom">Uncomfortable</div>
    </h1>
  </header>

  <div class="flyer__body">
    <div class="fan-photo" role="img" aria-label="Photo of a chrome ceiling fan with retractable clear blades and a light"></div>

    <div class="offer">
      <span class="offer__dollar">$</span>
      <span class="offer__save">SAVE</span>
      <span class="offer__amount">25</span>
      <span class="offer__off">OFF</span>
      <span class="offer__divider"></span>
      <div class="offer__deal">EVERY<br>2<sup>ND</sup> FAN<br>INSTALLED</div>
      <p class="offer__terms"><strong>Conditions:</strong> Mention this ad when booking to receive offer. Limit one per household. Cannot be combined with any other offer</p>
    </div>

    <div class="pitch">
      <h2 class="pitch__title">A breeze without the cost!</h2>
      <p class="pitch__text">Enjoy the gentle breeze &amp; cooling effect of a ceiling fan to help you sleep soundly at night &amp; be more productive during the day.</p>
    </div>
  </div>

  <footer class="flyer__footer">
    <div class="brand"><span class="brand__mark"></span><span class="brand__name">Bright<br>Spark</span></div>
    <div class="contact">
      <div class="contact__phone">1300 724 118</div>
      <div class="contact__web">www.brightsparkfans.com.au</div>
    </div>
    <span class="footer-divider"></span>
    <div class="payments" aria-label="Accepted cards"><span class="pay-a"></span><span class="pay-b"></span><span class="pay-c"></span></div>
    <div class="licence">lic no: 418265D</div>
  </footer>
</section>

<section class="flyer flyer--back">
  <header class="flyer__header">
    <h1 class="headline">
      <div class="headline__top"><span class="headline__hot">Hot</span> Sweaty</div>
      <div class="headline__bottom">Uncomfortable</div>
    </h1>
  </header>

  <div class="flyer__body">
    <div class="promises">
      <h2 class="promises__title">We guarantee to</h2>
      <ul class="promises__list">
        <li>Always be on time, or we pay you <strong>$100</strong></li>
        <li>Tell you the exact cost before any job begins</li>
        <li>Provide you with a fixed price guarantee,<br><span class="indent">assuring you have no extra costs</span></li>
        <li>Leave your place as clean as it was when we first arrived</li>
        <li>Return, and fix it for free, if its not right</li>
        <li>Return your telephone calls promptly</li>
        <li>Provide a minimum 12 Month warranty on all parts</li>
        <li>Provide friendly, helpful service and advice</li>
      </ul>
    </div>
    <div class="rule"></div>
    <div class="reviews">
      <div class="review">
        <p class="review__quote">“We can now sleep! Wow what a difference!<br>Thanks Daniel for your help.”</p>
        <p class="review__name">Marcus &amp; Clara Whitfield</p>
      </div>
      <div class="review">
        <p class="review__quote">“Super service! What a pleasant change. Daniel<br>could not have done more to ensure our satisfaction..”</p>
        <p class="review__name">Tom &amp; Rosa</p>
        <p class="review__place">Westbrook</p>
      </div>
    </div>
  </div>

  <footer class="flyer__footer">
    <div class="brand"><span class="brand__mark"></span><span class="brand__name">Bright<br>Spark</span></div>
    <div class="contact">
      <div class="contact__phone">1300 724 118</div>
      <div class="contact__web">www.brightsparkfans.com.au</div>
    </div>
    <span class="footer-divider"></span>
    <div class="payments" aria-label="Accepted cards"><span class="pay-a"></span><span class="pay-b"></span><span class="pay-c"></span></div>
    <div class="licence">lic no: 418265D</div>
  </footer>
</section>

</body>
</html>
```